" Clínica médica que atua nas diversas especialidades e realiza atendimentos particulares a preços acessíveis, podendo futuramente atender planos de saúde. "

```html
<!DOCTYPE html>
<html lang="pt-BR">
<head>
<meta charset="utf-8">
<title>ClíniVida – Quem Somos</title>
<link href="https://fonts.googleapis.com/css2?family=Raleway:wght@400;600;700;800&display=swap" rel="stylesheet">
<style>
  :root{
    --green-dark:#0f4f3a;
    --green-deep:#0b3b2c;
    --green-mid:#2f8a4e;
    --green-bright:#5fbf5a;
    --green-soft:#cfe8c9;
    --text-dark:#1e2b26;
    --text-muted:#6b7771;
    --white:#ffffff;
  }
  *{margin:0;padding:0;box-sizing:border-box}
  html,body{width:1200px;height:1200px;overflow:hidden;background:var(--white)}
  body{font-family:"Raleway",Arial,sans-serif;color:var(--text-dark);position:relative}
  .page{position:absolute;left:538px;top:12px;width:156px;height:1181px;background:var(--white);box-shadow:0 0 4px rgba(0,0,0,.12);display:flex;flex-direction:column}
  .page > *{flex-shrink:0}

  .topbar{height:29px;background:var(--green-dark);display:flex;align-items:center;justify-content:space-between;padding:0 7px}
  .brand{font-weight:700;font-size:8px;color:var(--white);display:flex;align-items:center;gap:3px}
  .brand-dot{width:6px;height:6px;border-radius:50%;background:var(--green-bright);flex-shrink:0}
  .topbar-note{font-size:3.4px;color:var(--green-soft);width:44px;text-align:right;line-height:1.3}

  .nav{height:50px;display:grid;grid-template-columns:1fr 1fr;align-content:center;padding:0 8px;gap:10px 10px;font-size:4.2px;font-weight:600;color:var(--text-dark);border-bottom:2px solid var(--green-dark)}
  .nav span{line-height:1.2}

  .about{height:130px;padding:15px 10px 0;display:flex;flex-direction:column}
  .about h1{font-size:10px;font-weight:800;margin-bottom:6px}
  .about .lead{font-size:6px;font-weight:600;color:var(--green-mid);line-height:1.3;margin-bottom:8px;width:96px}
  .about p{font-size:3.4px;color:var(--text-muted);line-height:1.45;width:128px}
  .about .about-brand{margin:auto auto 12px;display:flex;justify-content:center;align-items:center;gap:3px;font-size:9px;font-weight:700;color:var(--green-dark)}
  .about .about-brand .brand-dot{background:var(--green-mid);width:8px;height:8px}

  .photo{display:block;width:100%}
  .photo-building{height:134px;background:linear-gradient(100deg,#4d5e50 0%,#8c968f 30%,#d9ddd8 55%,#6a7269 80%,#3c4a3e 100%)}

  .mission{height:82px;background:linear-gradient(180deg,var(--green-mid),var(--green-bright));text-align:center;padding:14px 14px 0;color:var(--white)}
  .mission h2,.vision h2,.facilities h2{font-size:8.5px;font-weight:700;margin-bottom:6px}
  .mission p,.vision p{font-size:3.8px;line-height:1.5}

  .vision{height:62px;text-align:center;padding:8px 14px 0;color:var(--text-muted)}
  .vision h2{color:var(--green-mid);font-weight:600}

  .facilities{height:82px;background:linear-gradient(180deg,var(--green-soft),var(--green-bright));text-align:center;padding:12px 10px 0;color:var(--green-deep)}
  .facilities h2{line-height:1.15;margin-bottom:9px}
  .btn{display:inline-block;background:var(--green-dark);color:var(--white);font-size:3.6px;padding:2px 10px;font-weight:600}

  .photo-reception{height:115px;background:linear-gradient(180deg,#8a7a6a 0%,#d8cfc3 35%,#f1ede6 55%,#b49a80 100%)}
  .photo-hall{height:115px;background:linear-gradient(180deg,#c8ccca 0%,#f4f4f2 40%,#e3e4e1 70%,#9fa39f 100%)}
  .photo-room{height:113px;background:linear-gradient(180deg,#dde3e4 0%,#f5f7f7 45%,#c9d2d3 75%,#8f9c9c 100%)}

  .footer{flex:1 1 auto;background:linear-gradient(180deg,var(--green-dark),var(--green-deep));color:var(--white);padding:14px 8px 0;position:relative}
  .footer h3{font-size:8.5px;font-weight:700;letter-spacing:.3px}
  .footer .rule{height:1px;background:var(--green-bright);width:62px;margin:4px 0 7px}
  .contact-row{display:flex;justify-content:space-between}
  .contact{font-size:3.6px;line-height:1.6;color:var(--green-soft)}
  .contact strong{display:block;color:var(--white);font-size:4.6px;margin-bottom:1px}
  .social{margin-top:10px;width:58px}
  .social h4{font-size:7px;font-weight:700;line-height:1.05;margin-bottom:3px}
  .social h4 span{display:block;font-weight:400}
  .social-icons{display:flex;gap:2px}
  .social-icons i{width:7px;height:7px;background:var(--white);display:block;border-radius:1px}
  .sitemap{margin-top:14px}
  .sitemap-links{display:grid;grid-template-columns:1fr 1fr;gap:12px 6px;font-size:3.8px;color:var(--green-soft);width:96px;margin-top:4px}
  .footer-brand{position:absolute;right:10px;bottom:16px;font-size:11px;font-weight:700;color:var(--white);display:flex;align-items:center;gap:3px}
  .footer-brand .brand-dot{width:10px;height:10px}
</style>
</head>
<body>
  <main class="page">
    <header class="topbar">
      <div class="brand"><span class="brand-dot"></span>ClíniVida</div>
      <div class="topbar-note">Atendimento particular a preços acessíveis</div>
    </header>

    <nav class="nav">
      <span>Quem Somos</span><span>Exames</span>
      <span>Consultas<br>e Tratamentos</span><span>Fale Conosco</span>
    </nav>

    <section class="about">
      <h1>Quem Somos</h1>
      <div class="lead">Conheça mais da história da clínica referência em saúde</div>
      <p>Cuidamos da sua saúde com atenção, ética e especialistas dedicados em diversas áreas médicas.</p>
      <div class="about-brand"><span class="brand-dot"></span>ClíniVida</div>
    </section>

    <div class="photo photo-building" role="img" aria-label="Fachada moderna do prédio da clínica com vegetação"></div>

    <section class="mission">
      <h2>Nossa Missão</h2>
      <p>Cuidar de pessoas com excelência, oferecendo atendimento humano e acessível em todas as especialidades da clínica.</p>
    </section>

    <section class="vision">
      <h2>Nossa Visão</h2>
      <p>Ser uma referência em saúde, reconhecida pelo cuidado próximo e pela qualidade dos serviços prestados à comunidade.</p>
    </section>

    <section class="facilities">
      <h2>Instalações<br>e Diferenciais</h2>
      <span class="btn">Saiba</span>
    </section>

    <div class="photo photo-reception" role="img" aria-label="Recepção da clínica com balcão e poltronas"></div>
    <div class="photo photo-hall" role="img" aria-label="Corredor claro e amplo da clínica"></div>
    <div class="photo photo-room" role="img" aria-label="Sala de exames equipada"></div>

    <footer class="footer">
      <h3>CLÍNICA</h3>
      <div class="rule"></div>
      <div class="contact-row">
        <div class="contact">
          <strong>Bairro</strong>
          Rua das Acácias, 250<br>
          Centro – 00000-000<br>
          (00) 0000-0000<br>
          (00) 90000-0000<br>
          contato@clinivida.com.br<br>
          Seg a Sex, 7h às 19h
        </div>
        <div class="social">
          <h4>REDES<span>SOCIAIS</span></h4>
          <div class="social-icons"><i></i><i></i><i></i><i></i></div>
        </div>
      </div>
      <div class="sitemap">
        <h3>MAPA DO SITE</h3>
        <div class="rule"></div>
        <div class="sitemap-links">
          <span>Página Inicial</span><span>Quem Somos</span>
          <span>Nossa Saúde</span><span>Consultas</span>
          <span>Nossa Clínica</span><span>Tratamentos</span>
          <span>Fale Conosco</span><span>Perguntas Frequentes</span>
        </div>
      </div>
      <div class="footer-brand"><span class="brand-dot"></span>ClíniVida</div>
    </footer>
  </main>
</body>
</html>
```